3 Banners for Large Scale Print for Conference

We need 3 -32"x80" banners designed for a conference. The design needs to make it look as if the 3 separate units are one big unit. We will use this for a conference. We are a software firm that specializes in delivering online software to support customer surveys, assessments, and portals. From large corporations, to nonprofits, our software solutions are used to support their customer and stakeholder needs. I am attaching an example of how the 3 units could look so it flows like a single unit. I also attached an eps of our logo. It's in our colors of burgundy and silver.

Our corporate website is www.tervalinkworks.com . The design needs no bleed. I am looking for a professional awesome design.

I attached the eps of the logo which has the corporate colors and font. Take a look at the banner image I uploaded. I like how it done. Our words could be Survey, Assessment, Customer Engagement, Solutions, Secure Portals, Data Analysis, but we are open to creative ideas. Because the bottoms of the banners might be obscured but the table, I think an image might need to be there, but again I am open to your vision as long as it gives up a high-end upscale design.

Target Market(s)

Business Owners, Corporations, Nonprofits,

Industry/Entity Type

Software

Font styles to use
Sans Serif

Requirements
Must have
• The 3 banners must look like the form a larger image just with a gap because of them being 3 separate images. See the picture that I uploaded.
Should not have
• odd colors, amateur efforts. grainy images,

```html
<!DOCTYPE html>
<html lang="en">
<head>
<meta charset="utf-8">
<title>Terva Linkworks – Conference Banners</title>
<link rel="stylesheet" href="https://fonts.googleapis.com/css2?family=Arimo:wght@400;700&family=Questrial&display=swap">
<style>
  :root {
    --burgundy: #8a1a2c;
    --burgundy-dark: #6e1322;
    --ink: #3d3d42;
    --body-grey: #555a60;
    --stage: #d9dadc;
    --paper: #ffffff;
    --mist: #dfe8f1;
    --set-width: 1080px;
  }
  * { box-sizing: border-box; margin: 0; padding: 0; }
  html, body { width: 1200px; height: 960px; overflow: hidden; }
  body {
    background: var(--stage);
    font-family: "Arimo", Arial, sans-serif;
  }
  .banner-set {
    position: absolute;
    top: 80px;
    left: 60px;
    display: flex;
    gap: 60px;
  }
  .banner {
    position: relative;
    width: 320px;
    height: 800px;
    background: linear-gradient(to bottom, var(--paper) 55%, var(--mist) 100%);
    overflow: hidden;
    box-shadow: 0 6px 18px rgba(0,0,0,0.18);
  }
  .banner__photo {
    position: absolute;
    top: 0; left: 0;
    width: 100%;
    height: 310px;
    background-image: linear-gradient(100deg,
      #e6e9ec 0%, #c4c9cf 12%, #2b2b30 26%, #22242c 33%,
      #3c4b68 40%, #2a3550 52%, #4b5669 62%,
      #7f9fbf 72%, #d7e3ee 80%, #5a7ca2 90%, #2a3c58 100%);
    background-size: var(--set-width) 310px;
  }
  .banner__photo--office  { background-position: 0 0; }
  .banner__photo--network { background-position: -380px 0; }
  .banner__photo--servers { background-position: -760px 0; }
  .banner__wave {
    position: absolute;
    top: 262px; left: 0;
    width: 320px;
    height: 90px;
  }
  .banner__brand {
    position: absolute;
    top: 440px; left: 0;
    width: 100%;
    display: flex;
    justify-content: center;
    align-items: center;
    gap: 10px;
  }
  .banner__brand-dot {
    width: 16px; height: 16px;
    border-radius: 50%;
    background: var(--burgundy);
  }
  .banner__brand-name {
    font-family: "Questrial", Arial, sans-serif;
    font-size: 25px;
    letter-spacing: 0.5px;
    color: var(--ink);
  }
  .banner__copy {
    position: absolute;
    top: 520px; left: 24px;
    width: 272px;
    text-align: center;
  }
  .banner__headline {
    font-size: 19px;
    font-weight: 700;
    line-height: 1.25;
    color: var(--burgundy);
  }
  .banner__body {
    font-size: 14px;
    line-height: 1.32;
    color: var(--body-grey);
  }
  .banner__url-band {
    position: absolute;
    bottom: 0; left: 0;
    width: 100%;
    height: 56px;
    background: var(--burgundy);
    display: flex;
    align-items: center;
    justify-content: center;
  }
  .banner__url {
    font-size: 21px;
    color: var(--paper);
    letter-spacing: 0.3px;
  }
</style>
</head>
<body>
  <svg width="0" height="0" style="position:absolute" aria-hidden="true">
    <defs>
      <g id="set-wave">
        <path d="M0,50 C180,20 300,80 540,46 C780,12 900,78 1080,40 L1080,90 L0,90 Z" fill="#ffffff"/>
        <path d="M0,22 C180,-8 300,52 540,18 C780,-16 900,50 1080,12 L1080,34 C900,72 780,6 540,40 C300,74 180,14 0,44 Z" fill="#8a1a2c"/>
        <path d="M0,52 C180,22 300,82 540,48 C780,14 900,80 1080,42" fill="none" stroke="#6e1322" stroke-width="3"/>
      </g>
    </defs>
  </svg>

  <main class="banner-set">

    <section class="banner">
      <div class="banner__photo banner__photo--office" role="img" aria-label="Smiling businesswoman writing at a desk in a computer office, left part of a continuous scene"></div>
      <svg class="banner__wave" viewBox="0 0 320 90" preserveAspectRatio="none" aria-hidden="true"><use href="#set-wave"/></svg>
      <div class="banner__brand">
        <span class="banner__brand-dot"></span>
        <span class="banner__brand-name">TERVA LINKWORKS</span>
      </div>
      <div class="banner__copy">
        <h2 class="banner__headline">We are a software firm that specializes in</h2>
        <p class="banner__body">delivering online software to support customer surveys, assessments, and portals. From large corporations, to nonprofits, our software solutions are used to support their customer and stakeholder needs.</p>
      </div>
      <div class="banner__url-band"><span class="banner__url">www.tervalinkworks.com</span></div>
    </section>

    <section class="banner">
      <div class="banner__photo banner__photo--network" role="img" aria-label="Hand pointing at a network of people icons, centre part of a continuous scene"></div>
      <svg class="banner__wave" viewBox="380 0 320 90" preserveAspectRatio="none" aria-hidden="true"><use href="#set-wave"/></svg>
      <div class="banner__brand">
        <span class="banner__brand-dot"></span>
        <span class="banner__brand-name">TERVA LINKWORKS</span>
      </div>
      <div class="banner__copy">
        <h2 class="banner__headline">Surveys, Assessments &amp;<br>Customer Engagement</h2>
        <p class="banner__body">Listen to the people who matter most. Our online surveys and assessments capture clear, reliable feedback from customers, members and stakeholders, so every decision you make is built on what they really need.</p>
      </div>
      <div class="banner__url-band"><span class="banner__url">www.tervalinkworks.com</span></div>
    </section>

    <section class="banner">
      <div class="banner__photo banner__photo--servers" role="img" aria-label="Two technicians inspecting a server rack in a data centre, right part of a continuous scene"></div>
      <svg class="banner__wave" viewBox="760 0 320 90" preserveAspectRatio="none" aria-hidden="true"><use href="#set-wave"/></svg>
      <div class="banner__brand">
        <span class="banner__brand-dot"></span>
        <span class="banner__brand-name">TERVA LINKWORKS</span>
      </div>
      <div class="banner__copy">
        <h2 class="banner__headline">Secure Portals &amp;<br>Data Analysis</h2>
        <p class="banner__body">Give every customer and stakeholder a secure portal of their own. Our solutions turn the data you gather into clear reports and insight, helping corporations and nonprofits alike serve people better.</p>
      </div>
      <div class="banner__url-band"><span class="banner__url">www.tervalinkworks.com</span></div>
    </section>

  </main>
</body>
</html>
```